Postcard Design

www.tovil.com.au
i am an occupational therapist and professionally trained coach. i work with children, parents and disability service providers to achieve brilliant outcomes for children with special needs.
http://www.tovil.com.au/service/for-families
I need a postcard to give parents to promote our family service coaching service
A family service coach will work with you to set specific goals for your child, build a dream team, design and manage your child's highly effective therapy and educational team to ensure brilliant outcomes for your child..
KORBU - you have done my business card previously. they were great thank you.

```html
<!DOCTYPE html>
<html lang="en">
<head>
<meta charset="utf-8">
<title>Tovil Family Service Coaching Postcard</title>
<link rel="stylesheet" href="https://fonts.googleapis.com/css2?family=Oswald:wght@400;500&family=Josefin+Sans:wght@300;400&display=swap">
<style>
  :root {
    --brand-blue: #5b7fb9;
    --brand-blue-dark: #3f64a3;
    --sky-blue: #9fd8f7;
    --paper: #ffffff;
    --ink-navy: #1f2f55;
    --rule-grey: #c9c9c9;
    --backdrop: #ececec;
    --photo-navy: #232d45;
    --photo-sand: #b39675;
    --photo-sky: #dce8ee;
  }
  * { box-sizing: border-box; margin: 0; padding: 0; }
  html, body { width: 1200px; height: 787px; overflow: hidden; }
  body { background: var(--backdrop); position: relative; font-family: "Oswald", "Arial Narrow", sans-serif; }

  .postcard { position: absolute; background: var(--paper); box-shadow: 0 4px 14px rgba(0,0,0,.25); overflow: hidden; }

  /* Back side */
  .postcard--back { left: 22px; top: 62px; width: 604px; height: 480px; }
  .back__photo {
    position: absolute; left: 0; top: 0; width: 298px; height: 208px;
    background:
      radial-gradient(ellipse 30% 28% at 55% 50%, rgba(214,110,60,.75), rgba(214,110,60,0) 100%),
      radial-gradient(ellipse 50% 60% at 75% 35%, rgba(40,45,55,.8), rgba(40,45,55,0) 100%),
      linear-gradient(135deg, #8aa0b8 0%, #b7a89a 45%, #5f6f82 100%);
  }
  .back__stamp { position: absolute; left: 455px; top: 15px; width: 136px; height: 122px; border: 1px solid var(--rule-grey); }
  .back__address-line { position: absolute; left: 335px; width: 255px; height: 1px; background: var(--rule-grey); }
  .back__heading {
    position: absolute; left: 0; top: 218px; width: 308px; text-align: center;
    font-weight: 500; font-size: 17px; color: var(--ink-navy); letter-spacing: .2px;
  }
  .services { position: absolute; left: 30px; top: 248px; width: 260px; height: 90px; }
  .services__connector { position: absolute; left: 30px; top: 24px; width: 200px; height: 2px; background: var(--brand-blue); }
  .service { position: absolute; top: 0; width: 64px; text-align: center; }
  .service__icon { display: block; margin: 0 auto; width: 48px; height: 48px; }
  .service__label { display: block; margin-top: 4px; font-weight: 500; font-size: 11.5px; line-height: 1.05; color: var(--ink-navy); text-transform: uppercase; }
  .back__url-band {
    position: absolute; left: 0; top: 338px; width: 308px; height: 60px; background: var(--brand-blue);
    display: flex; align-items: center; justify-content: center;
    color: #fff; font-size: 13.5px; letter-spacing: .3px;
  }

  /* Front side */
  .postcard--front { left: 550px; top: 214px; width: 618px; height: 480px; }
  .front__photo {
    position: absolute; left: 0; top: 0; width: 618px; height: 416px;
    background:
      radial-gradient(ellipse 38% 62% at 86% 100%, var(--photo-navy) 0%, var(--photo-navy) 55%, rgba(35,45,69,0) 100%),
      radial-gradient(ellipse 30% 32% at 28% 48%, rgba(179,150,117,.9), rgba(179,150,117,0) 100%),
      radial-gradient(ellipse 20% 22% at 55% 40%, rgba(230,215,200,.9), rgba(230,215,200,0) 100%),
      linear-gradient(180deg, var(--photo-sky) 0%, #e8ecee 40%, #9a9ca3 68%, #3a4156 88%, #2a3147 100%);
  }
  .headline {
    position: absolute; left: 44px; top: 302px;
    font-family: "Josefin Sans", "Century Gothic", sans-serif; font-weight: 300;
    text-shadow: 0 1px 4px rgba(0,0,0,.6);
  }
  .headline__top { display: block; font-size: 29px; line-height: 1.1; color: #fff; }
  .headline__rule { position: absolute; left: -44px; top: 33px; width: 300px; height: 1px; background: #fff; }
  .headline__bottom { display: block; margin-top: 6px; font-size: 29px; line-height: 1.1; font-weight: 400; color: var(--sky-blue); }
  .front__band {
    position: absolute; left: 0; top: 416px; width: 618px; height: 64px; background: var(--brand-blue);
    display: flex; align-items: center; padding: 0 22px 0 18px; color: #fff;
  }
  .contact { display: flex; align-items: center; font-size: 22px; letter-spacing: .3px; margin-right: 18px; }
  .contact__icon { width: 20px; height: 20px; margin-right: 8px; }
  .wordmark { margin-left: auto; display: flex; align-items: center; font-size: 24px; font-weight: 400; color: #fff; }
  .wordmark__dot { width: 22px; height: 22px; border-radius: 50%; background: #fff; margin-right: 8px; }
</style>
</head>
<body>

<section class="postcard postcard--back" aria-label="Postcard back">
  <div class="back__photo" role="img" aria-label="Photo of hands joining coloured puzzle pieces"></div>
  <div class="back__stamp"></div>
  <div class="back__address-line" style="top:208px"></div>
  <div class="back__address-line" style="top:248px"></div>
  <div class="back__address-line" style="top:288px"></div>
  <div class="back__address-line" style="top:328px"></div>

  <h2 class="back__heading">A FAMILY SERVICE COACH PROVIDES:</h2>

  <div class="services">
    <div class="services__connector"></div>
    <div class="service" style="left:0">
      <svg class="service__icon" viewBox="0 0 48 48"><circle cx="24" cy="24" r="23" fill="var(--brand-blue)"/><circle cx="26" cy="22" r="12" fill="none" stroke="#fff" stroke-width="2.5"/><circle cx="26" cy="22" r="6" fill="none" stroke="#fff" stroke-width="2.5"/><path d="M12 36 L26 22" stroke="#fff" stroke-width="3"/></svg>
      <span class="service__label">Set goals</span>
    </div>
    <div class="service" style="left:64px">
      <svg class="service__icon" viewBox="0 0 48 48"><circle cx="24" cy="24" r="23" fill="var(--brand-blue)"/><circle cx="15" cy="15" r="3.5" fill="#fff"/><circle cx="24" cy="13" r="4" fill="#fff"/><circle cx="33" cy="15" r="3.5" fill="#fff"/><rect x="11.5" y="20" width="7" height="16" rx="3" fill="#fff"/><rect x="20" y="19" width="8" height="19" rx="3" fill="#fff"/><rect x="29.5" y="20" width="7" height="16" rx="3" fill="#fff"/></svg>
      <span class="service__label">Build a<br>dream team</span>
    </div>
    <div class="service" style="left:128px">
      <svg class="service__icon" viewBox="0 0 48 48"><circle cx="24" cy="24" r="23" fill="var(--brand-blue)"/><rect x="14" y="12" width="18" height="24" rx="2" fill="none" stroke="#fff" stroke-width="2.2"/><path d="M18 19h10M18 24h10M18 29h7" stroke="#fff" stroke-width="2"/><path d="M30 34 L37 20" stroke="#fff" stroke-width="3"/></svg>
      <span class="service__label">Design and<br>manage<br>therapy</span>
    </div>
    <div class="service" style="left:192px">
      <svg class="service__icon" viewBox="0 0 48 48"><circle cx="24" cy="24" r="23" fill="var(--brand-blue)"/><path d="M8 20 L24 13 L40 20 L24 27 Z" fill="#fff"/><path d="M15 24v7c4 4 14 4 18 0v-7l-9 4z" fill="#fff"/><path d="M37 21v9" stroke="#fff" stroke-width="1.6"/></svg>
      <span class="service__label">Educational<br>team</span>
    </div>
  </div>

  <div class="back__url-band">WWW.TOVIL.COM.AU/SERVICE/FOR-FAMILIES</div>
</section>

<section class="postcard postcard--front" aria-label="Postcard front">
  <div class="front__photo" role="img" aria-label="Photo of a smiling family with two young children and the coach in the foreground"></div>
  <h1 class="headline">
    <span class="headline__top">Ensure Brilliant</span>
    <span class="headline__rule"></span>
    <span class="headline__bottom">Outcomes For your child</span>
  </h1>
  <div class="front__band">
    <span class="contact">
      <svg class="contact__icon" viewBox="0 0 20 20"><circle cx="10" cy="10" r="10" fill="var(--brand-blue-dark)"/><circle cx="10" cy="10" r="3.2" fill="none" stroke="#fff" stroke-width="1.6"/><path d="M13.2 8v3a1.8 1.8 0 0 0 3.3 0A6.5 6.5 0 1 0 13 15.5" fill="none" stroke="#fff" stroke-width="1.6"/></svg>
      MIRA@TOVIL.COM.AU
    </span>
    <span class="contact">
      <svg class="contact__icon" viewBox="0 0 20 20"><circle cx="10" cy="10" r="10" fill="var(--brand-blue-dark)"/><path d="M7 5c-1 .5-2 1.5-1.5 3.5s3 5.5 5.5 6.5c1.6.6 2.6 0 3.3-.9l-2-2-1.4.8c-1-.5-2.6-2.1-3-3.1l.8-1.4z" fill="#fff"/></svg>
      0491 570 156
    </span>
    <span class="wordmark"><span class="wordmark__dot"></span>tovil</span>
  </div>
</section>

</body>
</html>
```